Sports Betting Business Consultant

After 21 years in corporate life. Will be continue as consultant/advisor in sports betting industry. Need a business card. Prefer an Zelvo format as layout. Elements; betting,ticket, sports types soccer, basketball, tennis etc , odds etc.

```html
<!DOCTYPE html>
<html lang="en">
<head>
<meta charset="UTF-8">
<title>Deniz Aral – Business Card</title>
<link href="https://fonts.googleapis.com/css2?family=Roboto+Slab:wght@300;400;800&family=Roboto:wght@400&display=swap" rel="stylesheet">
<style>
  :root {
    --page: #f4f4f5;
    --card: #c8c9cb;
    --card-edge: #b7b9bc;
    --bezel: #3a3a3a;
    --bezel-line: #555;
    --ink: #2f2f2f;
    --ink-soft: #555;
    --pill: rgba(255,255,255,0.18);
    --pill-edge: rgba(255,255,255,0.35);
    --mail-red: #c0392b;
    --call-blue: #4ea6e2;
  }
  * { box-sizing: border-box; margin: 0; padding: 0; }
  html, body { width: 1200px; height: 800px; overflow: hidden; background: var(--page); }
  .stage { width: 1200px; height: 800px; display: flex; align-items: center; justify-content: center; }
  .card {
    position: relative; width: 420px; height: 720px;
    background: var(--card); border: 1px solid var(--card-edge);
    border-radius: 26px; box-shadow: 0 10px 30px rgba(0,0,0,0.12);
  }
  .bezel {
    position: absolute; left: 14px; right: 14px; height: 136px;
    background: var(--bezel); border-radius: 20px;
  }
  .bezel-top { top: 14px; }
  .bezel-bottom { bottom: 14px; display: flex; align-items: center; justify-content: center; }
  .speaker { position: absolute; left: 130px; top: 74px; width: 130px; height: 6px; border-radius: 3px; background: var(--bezel-line); }
  .camera { position: absolute; left: 96px; top: 71px; width: 12px; height: 12px; border-radius: 50%; border: 3px solid var(--bezel-line); }
  .home-button { width: 66px; height: 66px; border-radius: 50%; border: 3px solid #6a6a6a; }
  .status-bar {
    position: absolute; top: 162px; left: 34px; right: 34px;
    display: flex; justify-content: space-between; align-items: center;
    font-family: "Roboto Slab", serif; font-size: 13px; color: var(--ink-soft);
  }
  .status-left, .status-right { display: flex; align-items: center; gap: 8px; }
  .lock-screen { position: absolute; top: 186px; left: 0; right: 0; text-align: center; color: var(--ink); }
  .clock { font-family: "Roboto Slab", serif; font-weight: 300; font-size: 96px; line-height: 1; text-shadow: 3px 3px 0 rgba(0,0,0,0.15); }
  .name { font-family: "Roboto Slab", serif; font-weight: 800; font-size: 46px; line-height: 1.15; margin-top: 4px; text-shadow: 3px 3px 0 rgba(0,0,0,0.15); }
  .title { font-family: "Roboto Slab", serif; font-weight: 400; font-size: 16px; color: var(--ink-soft); margin-top: 2px; }
  .contacts { position: absolute; top: 398px; left: 34px; right: 34px; display: flex; flex-direction: column; gap: 14px; }
  .contact {
    height: 62px; border-radius: 16px; background: var(--pill); border: 1px solid var(--pill-edge);
    display: flex; align-items: center; gap: 18px; padding: 0 16px;
    font-family: "Roboto", sans-serif; font-size: 24px; color: var(--ink);
  }
  .contact-icon { width: 40px; height: 40px; border-radius: 50%; display: flex; align-items: center; justify-content: center; flex: none; }
  .contact-icon.mail { background: var(--mail-red); }
  .contact-icon.call { background: var(--call-blue); }
</style>
</head>
<body>
<main class="stage">
  <article class="card">
    <div class="bezel bezel-top">
      <span class="camera"></span>
      <span class="speaker"></span>
    </div>

    <div class="status-bar">
      <div class="status-left">
        <svg width="22" height="16" viewBox="0 0 22 16" aria-label="signal">
          <rect x="0" y="11" width="4" height="5" fill="#3a3a3a"/>
          <rect x="6" y="8" width="4" height="8" fill="#3a3a3a"/>
          <rect x="12" y="4" width="4" height="12" fill="#3a3a3a"/>
          <rect x="18" y="0" width="4" height="16" fill="#3a3a3a"/>
        </svg>
        <svg width="22" height="16" viewBox="0 0 22 16" aria-label="wifi">
          <path d="M1 6 A14 14 0 0 1 21 6" fill="none" stroke="#3a3a3a" stroke-width="2.4"/>
          <path d="M5 10 A8 8 0 0 1 17 10" fill="none" stroke="#3a3a3a" stroke-width="2.4"/>
          <circle cx="11" cy="14" r="2" fill="#3a3a3a"/>
        </svg>
      </div>
      <div class="status-right">
        <span>100%</span>
        <svg width="30" height="14" viewBox="0 0 30 14" aria-label="battery">
          <rect x="1" y="1" width="25" height="12" rx="2" fill="none" stroke="#3a3a3a" stroke-width="1.6"/>
          <rect x="27" y="4.5" width="2.5" height="5" fill="#3a3a3a"/>
          <rect x="3.5" y="3.5" width="4" height="7" fill="#3a3a3a"/>
          <rect x="9" y="3.5" width="4" height="7" fill="#3a3a3a"/>
          <rect x="14.5" y="3.5" width="4" height="7" fill="#3a3a3a"/>
          <rect x="20" y="3.5" width="4" height="7" fill="#3a3a3a"/>
        </svg>
      </div>
    </div>

    <header class="lock-screen">
      <p class="clock">0:00</p>
      <h1 class="name">Deniz Aral</h1>
      <p class="title">Sports Betting Business Consultant</p>
    </header>

    <section class="contacts">
      <div class="contact">
        <span class="contact-icon mail">
          <svg width="22" height="16" viewBox="0 0 22 16" aria-label="email">
            <rect x="1" y="1" width="20" height="14" rx="1" fill="#fff"/>
            <path d="M1 1 L11 9 L21 1" fill="none" stroke="#c0392b" stroke-width="1.6"/>
          </svg>
        </span>
        <span>dnzarl @ mailbox</span>
      </div>
      <div class="contact">
        <span class="contact-icon call">
          <svg width="20" height="20" viewBox="0 0 24 24" aria-label="phone">
            <path d="M6.6 10.8a15 15 0 0 0 6.6 6.6l2.2-2.2a1 1 0 0 1 1-.25 11.4 11.4 0 0 0 3.6.57 1 1 0 0 1 1 1V20a1 1 0 0 1-1 1A17 17 0 0 1 3 4a1 1 0 0 1 1-1h3.5a1 1 0 0 1 1 1c0 1.25.2 2.45.57 3.57a1 1 0 0 1-.25 1z" fill="#fff"/>
          </svg>
        </span>
        <span>+90 555 0142287</span>
      </div>
    </section>

    <div class="bezel bezel-bottom">
      <span class="home-button"></span>
    </div>
  </article>
</main>
</body>
</html>
```